Overview of Elder Abuse Resources Brochure

We need a 2-page brochure that provides a list of resources for elders in tribal communities in the US and those who care for them. We want it to be simple and easy to read, and easy to see the difference between each resource. We would also like eye-catching images or graphics. Please keep the images on the front, and add any photos or graphics that depict Native American elders. We need both of our logos on the first page, in the far-right column. Please refer to the attached image for our brand colors and a font suggestion. Please keep the three columns on each page, but delete the blank pages in the document.

```html
<!DOCTYPE html>
<html lang="en">
<head>
<meta charset="utf-8">
<title>Elder Resources Brochure</title>
<link href="https://fonts.googleapis.com/css2?family=Poppins:ital,wght@0,400;0,500;0,600;0,700;1,400&display=swap" rel="stylesheet">
<style>
:root{
  --teal:#3b9da4;
  --teal-dark:#2f858b;
  --rust:#b4534a;
  --gold:#c9a86a;
  --ink:#222;
  --paper:#fff;
  --mist:#e6e6e6;
  --canvas:#d9d9d9;
}
*{box-sizing:border-box;margin:0;padding:0}
html,body{width:1200px;height:2190px;overflow:hidden}
body{background:var(--canvas);font-family:"Poppins",sans-serif;color:var(--ink);position:relative}
.page{position:absolute;left:30px;width:1140px;height:810px;background:var(--paper);box-shadow:0 6px 24px rgba(0,0,0,.18);overflow:hidden}
.page-outside{top:255px}
.page-inside{top:1125px}
.panel{position:absolute;top:0;width:380px;height:810px;overflow:hidden}
.p1{left:0}.p2{left:380px}.p3{left:760px}
.chevron-band{position:absolute;left:0;right:0;bottom:0;height:42px;background:linear-gradient(90deg,#f1d9d5,#c9786f 50%,var(--rust))}
/* outside left */
.respect{background:var(--teal);color:#fff;height:370px;padding:34px 34px 0 40px;position:relative}
.respect h1{font-size:27px;line-height:1.05;font-weight:700;letter-spacing:.5px}
.dove{position:absolute;right:36px;top:18px;width:105px;height:78px;background:rgba(255,255,255,.18);border-radius:8px}
.respect p{font-size:14.5px;line-height:1.35;margin-top:16px}
.help{padding:22px 34px 0 40px;font-size:14px;line-height:1.35}
.help h3{color:var(--rust);font-size:15px;font-weight:700}
.help .dept{color:var(--teal)}
.insert-box{background:var(--rust);color:#fff;font-style:italic;border-radius:5px;padding:9px 14px;margin:14px -6px 14px -10px;font-size:14px}
.help p{margin-top:14px}
.help .num{color:var(--rust);font-weight:700}
/* mailer */
.mailer{background:var(--paper)}
.mail-frame{position:absolute;left:14px;top:14px;right:14px;bottom:60px;border:2px solid var(--teal)}
.vert{position:absolute;writing-mode:vertical-rl;transform:rotate(180deg);font-size:15px;line-height:1.2}
.return-addr{left:20px;bottom:14px;color:var(--rust)}
.recipient{left:110px;top:360px;color:#111}
.recipient b{font-weight:700}
.web{right:20px;top:410px;color:var(--rust)}
.tel{right:20px;bottom:14px;color:var(--rust)}
.mail-logos{right:16px;top:20px;color:var(--teal);font-weight:600;font-size:16px}
/* cover */
.cover{background:linear-gradient(180deg,#d0d0d0,#ececec 60%,#e2e2e2)}
.logos{height:102px;display:flex;align-items:center;justify-content:center;gap:34px}
.logo-name{font-weight:700;font-size:26px;color:var(--teal);display:flex;align-items:center;gap:8px}
.logo-name.alt{color:var(--gold)}
.logo-name i{display:inline-block;width:12px;height:12px;background:currentColor}
.logo-rule{width:2px;height:60px;background:var(--teal)}
.photo{width:100%}
.cover .photo{height:258px;background:linear-gradient(160deg,#5a3f3a,#8a5b44 45%,#3a3634)}
.band-small{height:34px;background:linear-gradient(90deg,#c9786f,#e9c6c0 50%,#c9786f)}
.cover-title{background:var(--teal);color:#fff;text-align:center;padding:18px 20px 16px}
.cover-title h2{font-size:23px;line-height:1.15;font-weight:700}
.cover-title p{font-size:14px;margin-top:8px;opacity:.95}
.questions{list-style:none;padding:12px 34px 0 38px}
.questions li{position:relative;padding:10px 0 10px 28px;font-size:14.5px;line-height:1.3;border-bottom:1px solid #c8c8c8}
.questions li:last-child{border-bottom:none}
.questions li::before{content:"";position:absolute;left:0;top:15px;border-left:8px solid var(--rust);border-top:5px solid transparent;border-bottom:5px solid transparent}
/* inside */
.stories .photo{height:250px;background:linear-gradient(150deg,#6b2d3f,#a64a4a 50%,#3d2a3a)}
.stories-body{background:var(--teal);color:#fff;height:430px;padding:24px 30px 0 42px}
.stories-body h2{font-size:19px;font-weight:700;line-height:1.15}
.stories-body ul{list-style:none;margin-top:12px}
.stories-body li{position:relative;padding-left:18px;font-size:14px;line-height:1.3;margin-bottom:14px}
.stories-body li.dot::before{content:"";position:absolute;left:0;top:7px;width:5px;height:5px;border-radius:50%;background:#fff}
.help-now{background:var(--rust);color:#fff;height:88px;padding:14px 42px}
.help-now p{font-size:17px;opacity:.9}
.help-now strong{display:block;font-size:34px;line-height:1.1;font-weight:700}
.list{background:linear-gradient(90deg,#fff,#e4e4e4)}
.section-head{color:var(--teal);font-size:19px;font-weight:700;padding:30px 30px 0 32px}
.section-sub{color:var(--rust);font-style:italic;font-size:13px;padding:0 30px 0 32px}
.resource{margin:0 30px 0 32px;padding:11px 0;border-bottom:2px solid #cfd9da;font-size:13.3px;line-height:1.3;overflow-wrap:anywhere}
.resource:last-child{border-bottom:none}
.resource h3{color:var(--rust);font-size:14.5px;font-weight:600;line-height:1.25}
.resources-elders{padding-top:6px}
.caregivers{background:var(--paper)}
.care-box{background:#efefef;margin:12px 26px 14px 26px;padding:10px 18px;overflow:hidden}
.care-box .resource{margin:0;border:none;padding:8px 0}
.care-kicker{color:var(--rust);font-style:italic;font-size:13px;margin-top:6px}
.care-title{color:var(--teal);font-weight:600;font-size:14.5px;line-height:1.25;padding-bottom:8px;border-bottom:2px solid var(--teal)}
</style>
</head>
<body>

<section class="page page-outside">
  <div class="panel p1">
    <div class="respect">
      <h1>RESPECT<br>FOR ELDERS</h1>
      <div class="dove" role="img" aria-label="Line illustration of a dove carrying a branch"></div>
      <p>Do you have concerns about an Elder, maybe you see that they are not taking care of themselves, or family only comes once a month when the Elder has money?</p>
      <p>Is an Elder telling you that they are not treated with respect or that someone is bothering them?</p>
      <p>These may be signs of Elder abuse, neglect or exploitation.</p>
    </div>
    <div class="help">
      <h3>FOR HELP CONTACT:</h3>
      <div class="dept">Your Tribal Social Services or Elders Department:</div>
      <div class="insert-box">insert contact information for your tribal services, law enforcement, etc.</div>
      <p>The Elder Help Finder for information on Adult Protective Services<br><span class="num">1-800-555-0142</span></p>
      <p>If a serious emergency, call 911.</p>
      <p>For mental health support for yourself or an Elder, call or text 555-0199</p>
      <p>Family Safety Hotline<br><span class="num">1.800.555.0123</span></p>
    </div>
    <div class="chevron-band" role="img" aria-label="Decorative chevron pattern band"></div>
  </div>

  <div class="panel p2 mailer">
    <div class="mail-frame">
      <div class="vert return-addr">Company Name<br>Street Address<br>City, ST ZIP</div>
      <div class="vert recipient"><b>Recipient</b><br>Street Address<br>City, ST ZIP Code</div>
      <div class="vert web">Website<br>Email</div>
      <div class="vert tel">Tel Telephone<br>Fax Fax</div>
      <div class="vert mail-logos">COEA &nbsp;&nbsp; TEJP</div>
    </div>
    <div class="chevron-band" role="img" aria-label="Decorative chevron pattern band"></div>
  </div>

  <div class="panel p3 cover">
    <div class="logos">
      <span class="logo-name"><i></i>COEA</span>
      <span class="logo-rule"></span>
      <span class="logo-name alt">TEJP</span>
    </div>
    <div class="photo" role="img" aria-label="Photo of a smiling Native American elder woman wearing a headscarf"></div>
    <div class="band-small" role="img" aria-label="Decorative chevron pattern band"></div>
    <div class="cover-title">
      <h2>SERVICES FOR<br>ELDERS &amp; PEOPLE WHO<br>CARE FOR THEM</h2>
      <p>My Mother | My Father | My Sister<br>My Grandchild | Myself</p>
    </div>
    <ul class="questions">
      <li>Are you caring for an Elder or a Grandchild?</li>
      <li>Are you an Elder who needs help staying at home?</li>
      <li>These programs and information can be a helpful resource.</li>
    </ul>
    <div class="chevron-band" role="img" aria-label="Decorative chevron pattern band"></div>
  </div>
</section>

<section class="page page-inside">
  <div class="panel p1 stories">
    <div class="photo" role="img" aria-label="Photo of an elderly Native American woman wrapped in a patterned blanket"></div>
    <div class="stories-body">
      <h2>DO THESE STORIES SOUND FAMILIAR TO YOU?</h2>
      <ul>
        <li class="dot">My mother gets lost driving home from the store.</li>
        <li class="dot">I need help getting groceries and with chores at home.</li>
        <li class="dot">My dad wants to sleep all the time; he doesn’t go out with friends anymore. He stopped drumming.</li>
        <li class="dot">My sister is raising 3 grandchildren on her own.</li>
        <li>My son is disrespecting me. He only comes to visit when my retirement money arrives. He always asks for money.</li>
      </ul>
    </div>
    <div class="help-now">
      <p>Help is available...</p>
      <strong>1-800-555-0142</strong>
    </div>
    <div class="chevron-band" role="img" aria-label="Decorative chevron pattern band"></div>
  </div>

  <div class="panel p2 list">
    <h2 class="section-head">RESOURCES FOR ELDERS</h2>
    <div class="resources-elders">
      <div class="resource"><h3>Elder Help Finder</h3>https://elderhelpfinder.example.org<br>Call or Text: 1-800-555-0142<br>Email: help@elderhelpfinder.example.org<br>For help finding support. Ask about services to Tribal Elders.</div>
      <div class="resource"><h3>National Memory Care Line</h3>(24 hours 7 days a week)<br>Call 1-800-555-0177 For support for people living with dementia, caregivers, families and the public. Connect with a live person who can provide information, local resources, crisis assistance and emotional support.</div>
      <div class="resource"><h3>Crisis Support Line</h3>For mental health support, call or text 555-0199.</div>
      <div class="resource"><h3>State &amp; Tribal Hotlines | Tribal Elder Justice Project</h3>To find local resources within your tribe or state that specialize in elder abuse, neglect or exploitation, visit: https://coealliance.example.org/<wbr>tejp/<wbr>hotlines-codes/<wbr>state-tribal-hotlines/</div>
      <div class="resource"><h3>Bright Path Native Helpline</h3>A 24/7 safe, confidential and anonymous domestic and sexual violence helpline for Native Americans and Alaska Natives.<br>Call 1-844-555-0160<br>https://brightpathhelpline.example.org/</div>
    </div>
    <div class="chevron-band" role="img" aria-label="Decorative chevron pattern band"></div>
  </div>

  <div class="panel p3 caregivers">
    <h2 class="section-head">RESOURCES FOR CAREGIVERS</h2>
    <div class="section-sub">Caring for an Older Adult</div>
    <div class="care-box">
      <div class="resource"><h3>Elder Help Finder</h3>https://elderhelpfinder.example.org<br>Call or Text: 1-800-555-0142<br>Email: help@elderhelpfinder.example.org<br>For help finding support.<br>Ask about services to Tribal Elders.</div>
      <div class="resource"><h3>Memory Friends | Circle of Elders Alliance</h3>An interactive educational program to better understand what dementia is and how it affects people.<br>https://coealliance.example.org/<wbr>memory-friends/</div>
    </div>
    <div class="care-box">
      <div class="care-kicker">Caring for a Grandchild</div>
      <div class="care-title">Grandparents Raising Grandchildren (Kinship Care)</div>
      <div class="resource"><h3>KinFamiliesHub.org</h3>An interactive website that seeks to share all relevant publicly available information impacting grandfamilies.</div>
      <div class="resource"><h3>Grandparent Resources | Tribal Elder Justice Project</h3>A list of resources for grandparents raising grandchildren.<br>https://coealliance.example.org/<wbr>tejp/<wbr>resource/<wbr>grandparent-resources/</div>
    </div>
    <div class="chevron-band" role="img" aria-label="Decorative chevron pattern band"></div>
  </div>
</section>

</body>
</html>
```